Fresh, modern, fun business card for pediatric dental practice

Need a business card for fresh, modern, fun pediatric dental practice

Clean look that matches our website's font and colors

We prefer the look of curved corners on business cards

Target Market(s)

parents (mothers) of young children, professionals, mid-high class

Industry/Entity Type

Dental

Contact Information for Business Card

Maplebrook Pediatric Dentistry
482 Orchard Vale Road
Suite 517
Alderby, PA 17599
555.419.3067
www.maplebrookkidsdental.example

Mara Tevlin, DMD
Colette Varnum, DMD
(we are working on our email address, but we would like that on the card as well)

Font styles to use
Sans Serif

Requirements
Must have
• All info; we would also like to make cards for individual staff members
• colors from our website and color palatte, attatched
• use same font and design as website for branding
Nice to have
• clean, simple card that has a pop of color
• we would like to see a few designs with our tag line "where smiles get brighter"
• we are not sure if we want to have it on there or not
• we would like to see a few designs incorporating the ribbon graphic on our website where the word WELCOME is

```html
<!DOCTYPE html>
<html lang="en">
<head>
<meta charset="utf-8">
<title>Maplebrook Pediatric Dentistry – Business Card</title>
<link rel="stylesheet" href="https://fonts.googleapis.com/css2?family=Lato:wght@400;700&family=Raleway:wght@500;600&display=swap">
<style>
  :root {
    --backdrop: #000000;
    --paper: #f2f2f2;
    --sun: #f6bb27;
    --berry: #c81f84;
    --ink: #2b2b2b;
    --white: #ffffff;
  }
  * { box-sizing: border-box; margin: 0; padding: 0; }
  html, body {
    width: 1200px; height: 900px; overflow: hidden;
    background: var(--backdrop);
  }
  .stage { position: relative; width: 1200px; height: 900px; }

  .card { position: absolute; top: 200px; width: 310px; height: 502px; }

  .card--front {
    left: 265px;
    background: var(--paper);
    border-radius: 52px 0 52px 0;
  }
  .card--back {
    left: 641px;
    background: var(--sun);
    border-radius: 0 52px 0 52px;
  }

  /* wordmark */
  .wordmark {
    position: absolute; left: 0; right: 0; top: 96px;
    text-align: center;
    font-family: "Lato", sans-serif;
  }
  .wordmark__dot {
    display: block; width: 38px; height: 38px; border-radius: 50%;
    background: var(--sun); margin: 0 auto 12px;
  }
  .wordmark__name {
    font-size: 38px; line-height: 40px; font-weight: 700;
    letter-spacing: 1px; color: var(--sun);
  }
  .wordmark__line {
    font-size: 20px; line-height: 24px; font-weight: 400;
    letter-spacing: 1.2px; color: var(--berry);
  }

  .wordmark--back {
    top: auto; bottom: 62px; left: 34px; right: auto; text-align: left;
  }
  .wordmark--back .wordmark__name { font-size: 40px; line-height: 42px; color: var(--white); }
  .wordmark--back .wordmark__line { font-size: 20px; color: var(--white); }

  /* doctors */
  .doctors {
    position: absolute; left: 25px; top: 280px;
    font-family: "Raleway", sans-serif; font-weight: 600;
    font-size: 18.5px; line-height: 22px; list-style: none;
  }
  .doctors__first { color: var(--berry); }
  .doctors__last { color: var(--sun); }
  .doctors__title { color: var(--sun); font-size: 14px; font-weight: 500; }

  .address {
    position: absolute; left: 25px; top: 340px;
    font-family: "Lato", sans-serif; font-style: normal;
    font-size: 13.5px; line-height: 21px; color: var(--ink);
  }

  .contacts {
    position: absolute; left: 25px; top: 390px; list-style: none;
    font-family: "Lato", sans-serif; font-size: 13.5px; line-height: 20.7px; color: var(--ink);
  }
  .contacts li { display: flex; align-items: center; gap: 8px; white-space: nowrap; }
  .contacts svg { width: 10px; height: 10px; flex: none; }
  .icon-fill { fill: var(--sun); }
  .icon-fold { fill: none; stroke: var(--paper); stroke-width: 0.9; }
</style>
</head>
<body>
<main class="stage">

  <section class="card card--front" aria-label="Business card front">
    <div class="wordmark">
      <span class="wordmark__dot" aria-hidden="true"></span>
      <div class="wordmark__name">maplebrook</div>
      <div class="wordmark__line">pediatric dentistry</div>
    </div>

    <ul class="doctors">
      <li><span class="doctors__first">Mara</span> <span class="doctors__last">Tevlin,</span> <span class="doctors__title">DMD</span></li>
      <li><span class="doctors__first">Colette</span> <span class="doctors__last">Varnum,</span> <span class="doctors__title">DMD</span></li>
    </ul>

    <address class="address">
      482 Orchard Vale Road<br>
      Suite 517 Alderby, PA 17599
    </address>

    <ul class="contacts">
      <li>
        <svg viewBox="0 0 10 10" aria-hidden="true"><path class="icon-fill" d="M2 0.5 L3.6 2.6 L2.7 3.8 Q3.9 6.2 6.2 7.3 L7.4 6.4 L9.5 8 L8.3 9.5 Q3.8 9.3 0.5 1.7 Z"/></svg>
        555.419.3067
      </li>
      <li>
        <svg viewBox="0 0 10 10" aria-hidden="true"><rect class="icon-fill" x="0.5" y="2" width="9" height="6.5"/><path class="icon-fold" d="M0.8 2.3 L5 5.6 L9.2 2.3"/></svg>
        mara@maplebrookkidsdental.example
      </li>
      <li>
        <svg viewBox="0 0 10 10" aria-hidden="true"><rect class="icon-fill" x="0.5" y="2" width="9" height="6.5"/><path class="icon-fold" d="M0.8 2.3 L5 5.6 L9.2 2.3"/></svg>
        colette@maplebrookkidsdental.example
      </li>
      <li>
        <svg viewBox="0 0 10 10" aria-hidden="true"><circle class="icon-fill" cx="5" cy="5" r="4.6"/></svg>
        www.maplebrookkidsdental.example
      </li>
    </ul>
  </section>

  <section class="card card--back" aria-label="Business card back">
    <div class="wordmark wordmark--back">
      <div class="wordmark__name">maplebrook</div>
      <div class="wordmark__line">pediatric dentistry</div>
    </div>
  </section>

</main>
</body>
</html>
```